Business card design for sports medicine and athlete care clinic.

We need a bold, solid business card design for our practitioners to stand out. We treat overuse & sports-related injuries and provide post-operative rehabilitation. Our specialisations include chronic conditions, men’s health, nutrition & musculoskeletal disorders (MSDs). All brand collateral in terms of fonts, logo and colour palette to be provided.

Target Market(s)

Athletes (professional and amateur), sportspeople, predominantly male

Industry/Entity Type

Health And Wellness

Contact Information for Business Card

The front of the card should be white with dark blue text the back dark blue with white text. The logo should be top-left. The business name should be horizontal and right of the logo. The tagline should be directly below centred on the back of the card (see top-banner.png and bottom-banner.png)

Font styles to use
Sans Serif

Colors
0355a3
0293ce
3176b5
ffffff
85acd3

Requirements
Nice to have
• Diagonal and/or horizontal line elements between logo and practitioner details and/or bottom corner of card (see slide.png and tag-bg.png).

```html
<!DOCTYPE html>
<html lang="en">
<head>
<meta charset="utf-8">
<title>The Runner's Lodge – Business Card</title>
<link rel="stylesheet" href="https://fonts.googleapis.com/css2?family=Montserrat:wght@400;500;700;800&display=swap">
<style>
  :root {
    --navy: #22215a;
    --ink: #1f1e57;
    --sky: #0293ce;
    --mid-blue: #3176b5;
    --deep-blue: #0355a3;
    --pale-blue: #85acd3;
    --white: #ffffff;
    --slate: #454749;
    --backdrop: #1c1d20;
  }
  * { box-sizing: border-box; margin: 0; padding: 0; }
  html, body {
    width: 1200px; height: 948px; overflow: hidden;
    background: var(--backdrop);
    font-family: "Montserrat", sans-serif;
  }
  .canvas {
    position: relative; width: 1200px; height: 948px;
    display: flex; flex-direction: column; align-items: center; justify-content: center; gap: 50px;
  }
  .card {
    position: relative; width: 620px; height: 354px;
    border-radius: 22px; overflow: hidden;
  }

  /* Back of card */
  .card--back { background: var(--navy); color: var(--white); text-align: center; }
  .card--back .logo-figure {
    position: absolute; left: 262px; top: 40px; width: 96px; height: 130px;
    border-radius: 40px 40px 20px 20px;
    background: linear-gradient(160deg, var(--sky), var(--mid-blue) 60%, var(--pale-blue));
  }
  .card--back .brand-name {
    position: absolute; left: 0; right: 0; top: 186px;
    font-weight: 800; font-size: 40px; letter-spacing: 0.5px; color: var(--white);
  }
  .card--back .tagline {
    position: absolute; left: 0; right: 0; top: 240px;
    font-weight: 500; font-size: 15px; letter-spacing: 3px; color: var(--sky);
  }

  /* Front of card */
  .card--front { background: var(--white); color: var(--ink); }
  .card--front .bands { position: absolute; inset: 0; }
  .card--front .logo-figure {
    position: absolute; left: 128px; top: 22px; width: 62px; height: 96px;
    border-radius: 26px 26px 12px 12px;
    background: linear-gradient(160deg, var(--sky), var(--mid-blue) 55%, var(--ink));
  }
  .card--front .brand-name {
    position: absolute; left: 204px; top: 24px;
    font-weight: 800; font-size: 34px; color: var(--ink); white-space: nowrap;
  }
  .card--front .tagline {
    position: absolute; left: 222px; top: 70px;
    font-weight: 500; font-size: 13px; letter-spacing: 2.4px; color: var(--sky); white-space: nowrap;
  }
  .person { position: absolute; left: 262px; top: 112px; }
  .person-name { font-weight: 800; font-size: 21px; color: var(--ink); letter-spacing: 0.3px; }
  .person-role { font-weight: 500; font-size: 13px; color: var(--ink); margin-top: 2px; }
  .divider {
    position: absolute; left: 258px; top: 170px; width: 320px; height: 1.5px; background: var(--sky);
  }
  .contacts { position: absolute; left: 268px; top: 184px; list-style: none; }
  .contact {
    display: flex; align-items: center; gap: 10px;
    font-weight: 400; font-size: 14.5px; color: var(--ink); height: 27px; white-space: nowrap;
  }
  .contact svg { width: 13px; height: 13px; flex: none; }
  .social-dot { width: 13px; height: 13px; border-radius: 50%; background: var(--ink); flex: none; }
</style>
</head>
<body>
<main class="canvas">

  <section class="card card--back" aria-label="Card back">
    <div class="logo-figure" role="img" aria-label="Brand emblem: stylised running athlete in shades of blue"></div>
    <p class="brand-name">The Runner's Lodge</p>
    <p class="tagline">Sports medicine and athlete care</p>
  </section>

  <section class="card card--front" aria-label="Card front">
    <svg class="bands" viewBox="0 0 620 354" aria-hidden="true">
      <polyline points="28,-10 62,236 300,370" fill="none" stroke="var(--slate)" stroke-width="15" stroke-linejoin="miter"/>
      <polyline points="56,-10 90,218 350,370" fill="none" stroke="var(--sky)" stroke-width="17" stroke-linejoin="miter"/>
    </svg>

    <div class="logo-figure" role="img" aria-label="Brand emblem: stylised running athlete in shades of blue"></div>
    <p class="brand-name">The Runner's Lodge</p>
    <p class="tagline">Sports medicine and athlete care</p>

    <div class="person">
      <p class="person-name">DANIEL REYES</p>
      <p class="person-role">Owner/CEO</p>
    </div>
    <div class="divider"></div>

    <ul class="contacts">
      <li class="contact">
        <svg viewBox="0 0 16 16"><path d="M4 1l3 3-2 2c1 2 3 4 5 5l2-2 3 3-2 3C7 15 1 9 1 3z" fill="var(--ink)"/></svg>
        555-210-4821
      </li>
      <li class="contact">
        <svg viewBox="0 0 16 16"><rect x="1" y="3" width="14" height="10" fill="var(--ink)"/><path d="M1 3l7 6 7-6" fill="none" stroke="var(--white)" stroke-width="1.3"/></svg>
        info@therunnerslodge.com.au
      </li>
      <li class="contact">
        <svg viewBox="0 0 16 16"><circle cx="8" cy="8" r="6.5" fill="none" stroke="var(--ink)" stroke-width="1.5"/><path d="M1.5 8h13M8 1.5c-3 3-3 10 0 13M8 1.5c3 3 3 10 0 13" fill="none" stroke="var(--ink)" stroke-width="1.2"/></svg>
        www.therunnerslodge.com.au
      </li>
      <li class="contact">
        <span class="social-dot"></span>
        RunnersLodgeAU
      </li>
    </ul>
  </section>

</main>
</body>
</html>
```